Byteway Tech Services Flyer

I have a retail Computer Store that I want to promote in the local area.
The target market is seniors aged between 40-80 year olds. I need to create a flyer for the business to do a flyer drop to homes and business advertising the business & services we offer. I would also like to drop this on our socials for online target ads.
Store Name: Byteway Tech systems Address: 17 Larkspur Road, DONVALE Victoria 3111 Phone Number: (03) 9521 6408 Target Audience: older generation between 40 - 90 year olds Services offered: Retail Sales & Service, Complete Workshop Facilities, Cloud services, Deskly 240 Experts, Network & Wireless Products, Managed Services, PC & Laptop Sales, Custom Built Computers Vendors: Veltrix, QORNL, Parvanix Partner, Olex, Brimo, KT & Rune Reseller Please keep it to A1 size and double sided with options to go A3 o A4 later.

Target Market(s)

Residential home users

Industry/Entity Type

www.bytewaytech.com.au

Font styles to use
Sans Serif

Colors
0054AA
0677BA
7BADD7
CADEEF
E8F1F8

Requirements
Must have
• Simple target is the elderly population

```html
<!DOCTYPE html>
<html lang="en">
<head>
<meta charset="utf-8">
<title>Byteway Tech Systems Flyer</title>
<link href="https://fonts.googleapis.com/css2?family=Lato:wght@400;700;900&display=swap" rel="stylesheet">
<style>
  :root {
    --page-bg: #ececec;
    --sheet-bg: #ffffff;
    --title-teal: #1c4a58;
    --brand-navy: #1f3f78;
    --body-grey: #3a3a3a;
    --help-blue: #2a7fc0;
    --tile-blue: #3a7cb8;
    --tile-teal: #4ea9b1;
    --tile-sea: #2ea58f;
    --tile-green: #7cb64a;
    --mark-blue: #0677BA;
    --white: #ffffff;
  }
  * { margin: 0; padding: 0; box-sizing: border-box; }
  html, body {
    width: 1200px; height: 1200px; overflow: hidden;
    background: var(--page-bg);
    font-family: "Lato", Arial, sans-serif;
  }
  .flyer {
    position: absolute; left: 239px; top: 86px;
    width: 722px; height: 1028px;
    background: var(--sheet-bg);
    text-align: center;
  }
  .headline {
    position: absolute; left: 0; right: 0; top: 43px;
    font-size: 52px; font-weight: 700; line-height: 58px;
    color: var(--title-teal);
  }
  .subhead {
    position: absolute; left: 0; right: 0; top: 172px;
    font-size: 20px; color: var(--body-grey);
  }
  .brand {
    position: absolute; left: 0; right: 0; top: 255px; height: 56px;
    display: flex; justify-content: center; align-items: center; gap: 16px;
  }
  .brand-square {
    width: 56px; height: 56px; border-radius: 8px;
    background: var(--mark-blue);
  }
  .brand-name {
    font-size: 47px; font-weight: 700; color: var(--brand-navy);
  }
  .tagline {
    position: absolute; left: 0; right: 0; top: 312px;
    font-size: 24px; color: var(--body-grey); padding-left: 70px;
  }
  .service-grid {
    position: absolute; left: 113px; top: 392px;
    display: grid; grid-template-columns: 235px 235px;
    grid-auto-rows: 192px; gap: 24px 26px;
  }
  .service-tile {
    border-radius: 20px; color: var(--white);
    display: flex; flex-direction: column; align-items: center;
    padding-top: 30px;
  }
  .service-tile svg { width: 80px; height: 80px; }
  .service-tile p {
    margin-top: 18px; font-size: 19px; font-weight: 700; line-height: 26px;
  }
  .tile-computer { background: var(--tile-blue); }
  .tile-security { background: var(--tile-teal); }
  .tile-internet { background: var(--tile-sea); }
  .tile-laptop   { background: var(--tile-green); }
  .help-line {
    position: absolute; left: 0; right: 0; top: 845px;
    font-size: 35px; font-weight: 700; color: var(--help-blue);
  }
  .phone {
    position: absolute; left: 0; right: 0; top: 890px;
    font-size: 52px; font-weight: 700; color: var(--body-grey);
  }
  .address {
    position: absolute; left: 0; right: 0; top: 956px;
    font-size: 21px; color: var(--body-grey);
  }
</style>
</head>
<body>
<main class="flyer">
  <h1 class="headline">Is Technology<br>Leaving You Behind?</h1>
  <p class="subhead">Expert Computer Help for Donvale &amp; Surrounds</p>

  <div class="brand">
    <span class="brand-square"></span>
    <span class="brand-name">Byteway Tech Systems</span>
  </div>
  <p class="tagline">Your Local Tech Experts for Peace of Mind</p>

  <section class="service-grid">
    <div class="service-tile tile-computer">
      <svg viewBox="0 0 80 80" fill="none" stroke="#fff" stroke-width="6" stroke-linecap="round">
        <circle cx="32" cy="32" r="20"/>
        <line x1="47" y1="47" x2="68" y2="68" stroke-width="9"/>
      </svg>
      <p>Having Trouble with<br>Your Computer?</p>
    </div>
    <div class="service-tile tile-security">
      <svg viewBox="0 0 80 80" fill="none" stroke="#fff" stroke-width="5" stroke-linejoin="round">
        <path d="M40 6 L68 16 V38 C68 56 56 68 40 75 C24 68 12 56 12 38 V16 Z"/>
        <path d="M40 14 V68 C28 62 20 52 20 38 V22 Z" fill="#fff" stroke="none" opacity="0.9"/>
        <circle cx="40" cy="36" r="7" fill="#fff" stroke="none"/>
        <rect x="30" y="38" width="20" height="16" rx="3" fill="#fff" stroke="none"/>
        <circle cx="40" cy="44" r="3" fill="#4ea9b1" stroke="none"/>
      </svg>
      <p>Worried About Online<br>Security?</p>
    </div>
    <div class="service-tile tile-internet">
      <svg viewBox="0 0 80 80" fill="none" stroke="#fff" stroke-width="6" stroke-linecap="round">
        <path d="M8 30 C26 12 54 12 72 30"/>
        <path d="M18 41 C30 29 50 29 62 41"/>
        <circle cx="40" cy="56" r="6" fill="#fff" stroke="none"/>
        <line x1="50" y1="62" x2="70" y2="62" stroke-width="5"/>
        <path d="M63 54 L72 62 L63 70" stroke-width="5"/>
      </svg>
      <p>Internet Not<br>Working Right?</p>
    </div>
    <div class="service-tile tile-laptop">
      <svg viewBox="0 0 80 80" fill="none" stroke="#fff" stroke-width="4" stroke-linejoin="round">
        <rect x="4" y="34" width="30" height="32" fill="#fff" stroke="none"/>
        <rect x="2" y="26" width="34" height="10" fill="#fff" stroke="none"/>
        <line x1="19" y1="26" x2="19" y2="66" stroke="#7cb64a"/>
        <path d="M19 26 C12 14 6 20 12 24 M19 26 C26 14 32 20 26 24"/>
        <rect x="40" y="18" width="34" height="40" rx="2"/>
        <line x1="36" y1="64" x2="78" y2="64"/>
      </svg>
      <p>Looking for New<br>PC or Laptop?</p>
    </div>
  </section>

  <p class="help-line">We’re Here to Help!</p>
  <p class="phone">(03) 9521 6408</p>
  <p class="address">17 Larkspur Road, DONVALE Victoria 3111</p>
</main>
</body>
</html>
```